Bamboo Toothbrush packaging design

We need a packaging design for a pack of 4 bamboo toothbrushes. The front of the package would need to include the company logo, name of the product - Bamboo Toothbrush, 100% plastic free, and 10% of profit will go to environmental charities . Would like to see some simple or creative graphics to send the message.

Target Market(s)

Retail

Font styles to use
Sans Serif

Colors

Designer to choose colors to be used in the design.

Requirements
Must have
• Just be creative.

```html
<!DOCTYPE html>
<html lang="en">
<head>
<meta charset="utf-8">
<title>Tern Valley Bamboo Toothbrush – Box Dieline</title>
<link href="https://fonts.googleapis.com/css2?family=Roboto:wght@400;500&family=Roboto+Condensed:wght@400;500;700&display=swap" rel="stylesheet">
<style>
  :root {
    --ink: #1e333d;
    --paper: #ffffff;
    --cut: #9a9a9a;
    --bg: #ffffff;
  }
  html, body {
    margin: 0;
    padding: 0;
    width: 1200px;
    height: 1000px;
    overflow: hidden;
    background: var(--bg);
  }
  .dieline { display: block; width: 1200px; height: 1000px; }
  .panel-dark { fill: var(--ink); }
  .panel-light { fill: var(--paper); stroke: var(--cut); stroke-width: 1; }
  .flap-outline { fill: var(--paper); stroke: var(--cut); stroke-width: 1; }
  .brand-name { font-family: "Roboto", sans-serif; font-weight: 400; font-size: 27px; fill: var(--paper); }
  .brand-name-small { font-family: "Roboto", sans-serif; font-weight: 400; font-size: 12px; }
  .product-title { font-family: "Roboto Condensed", sans-serif; font-weight: 500; font-size: 25px; fill: var(--ink); letter-spacing: 0.3px; }
  .profit-title { font-family: "Roboto Condensed", sans-serif; font-weight: 500; font-size: 14px; fill: var(--ink); }
  .profit-note { font-family: "Roboto Condensed", sans-serif; font-weight: 400; font-size: 6px; fill: var(--ink); }
  .claim { font-family: "Roboto", sans-serif; font-weight: 400; font-size: 14px; fill: var(--ink); }
  .badge { fill: var(--paper); }
  .badge-text { font-family: "Roboto Condensed", sans-serif; font-weight: 700; font-size: 6px; fill: var(--ink); }
  .badge-eco { font-family: "Roboto Condensed", sans-serif; font-weight: 700; font-size: 10px; fill: var(--paper); }
  .badge-friendly { font-family: "Roboto Condensed", sans-serif; font-weight: 500; font-size: 8px; fill: var(--ink); }
  .pack-badge { fill: var(--ink); }
  .pack-num { font-family: "Roboto", sans-serif; font-size: 11px; fill: var(--paper); }
  .pack-word { font-family: "Roboto", sans-serif; font-size: 6px; fill: var(--paper); }
  .bamboo-art { fill: var(--ink); }
</style>
</head>
<body>
<svg class="dieline" viewBox="0 0 1200 1000" xmlns="http://www.w3.org/2000/svg">
  <g transform="translate(0,-238)">

    <!-- Row 1: side panel -->
    <rect class="panel-dark" x="243" y="575" width="276" height="55"/>
    <rect class="panel-light" x="519" y="575" width="403" height="55"/>
    <rect class="flap-outline" x="922" y="577" width="36" height="53"/>

    <!-- Row 2: front panel with left tuck flap -->
    <path class="panel-dark" d="M243 633 L183 633 Q172 633 172 645 L172 716 L243 716 Z"/>
    <line x1="221" y1="633" x2="221" y2="716" stroke="#2c4752" stroke-width="1"/>
    <rect class="panel-dark" x="243" y="630" width="276" height="86"/>
    <rect class="panel-light" x="519" y="630" width="439" height="86"/>

    <!-- Row 3: side panel -->
    <rect class="panel-dark" x="243" y="716" width="276" height="56"/>
    <rect class="panel-light" x="519" y="716" width="439" height="56"/>

    <!-- Row 4: back panel with right tuck flap -->
    <rect class="panel-dark" x="278" y="772" width="241" height="85"/>
    <rect class="panel-light" x="519" y="772" width="403" height="85"/>
    <path class="flap-outline" d="M922 775 L1018 775 Q1030 775 1030 787 L1030 845 Q1030 857 1018 857 L922 857"/>
    <line x1="978" y1="775" x2="978" y2="857" stroke="var(--cut)" stroke-width="1"/>

    <!-- Glue flap -->
    <path class="panel-dark" d="M278 857 L519 857 L519 900 L290 900 Z"/>
    <path class="panel-light" d="M519 857 L922 857 L905 900 L519 900 Z"/>

    <!-- Brand names -->
    <text class="brand-name" x="398" y="699" text-anchor="middle">Tern Valley</text>
    <text class="brand-name" x="398" y="842" text-anchor="middle">Tern Valley</text>
    <text class="brand-name-small" transform="translate(236,674) rotate(90)" text-anchor="middle" fill="var(--paper)">Tern Valley</text>
    <text class="brand-name-small" transform="translate(940,816) rotate(90)" text-anchor="middle" fill="var(--ink)">Tern Valley</text>

    <!-- Badge rows -->
    <g class="badge-row">
      <rect class="badge" x="305" y="591" width="48" height="24" rx="3"/>
      <rect class="bamboo-art" x="309" y="594" width="10" height="18" role="img" aria-label="Small bamboo stalk icon"/>
      <text class="badge-text" x="322" y="606">BANBOO</text>
      <rect class="badge" x="374" y="591" width="48" height="24" rx="3"/>
      <rect x="376" y="593" width="44" height="10" rx="2" fill="var(--ink)"/>
      <text class="badge-eco" x="398" y="602" text-anchor="middle">ECO</text>
      <text class="badge-friendly" x="398" y="612" text-anchor="middle">FRIENDLY</text>
      <rect class="badge" x="443" y="591" width="48" height="24" rx="3"/>
      <circle cx="454" cy="603" r="5" fill="none" stroke="var(--ink)" stroke-width="1.5"/>
      <text class="badge-text" x="463" y="606">RECYCLE</text>
    </g>
    <g class="badge-row">
      <rect class="badge" x="305" y="732" width="48" height="24" rx="3"/>
      <rect class="bamboo-art" x="309" y="735" width="10" height="18" role="img" aria-label="Small bamboo stalk icon"/>
      <text class="badge-text" x="322" y="747">BANBOO</text>
      <rect class="badge" x="374" y="732" width="48" height="24" rx="3"/>
      <rect x="376" y="734" width="44" height="10" rx="2" fill="var(--ink)"/>
      <text class="badge-eco" x="398" y="743" text-anchor="middle">ECO</text>
      <text class="badge-friendly" x="398" y="753" text-anchor="middle">FRIENDLY</text>
      <rect class="badge" x="443" y="732" width="48" height="24" rx="3"/>
      <circle cx="454" cy="744" r="5" fill="none" stroke="var(--ink)" stroke-width="1.5"/>
      <text class="badge-text" x="463" y="747">RECYCLE</text>
    </g>

    <!-- Side panel messages -->
    <text class="profit-title" x="548" y="607">10% OF PROFIT</text>
    <text class="profit-note" x="548" y="614">GO TO ENVIRONMENTAL CHARITIES</text>
    <rect class="bamboo-art" x="665" y="581" width="20" height="44" opacity="0.85" role="img" aria-label="Small bamboo sprig illustration"/>
    <text class="claim" x="697" y="608">100% natural banboo toothbrush</text>

    <text class="profit-title" x="548" y="748">10% OF PROFIT</text>
    <text class="profit-note" x="548" y="755">GO TO ENVIRONMENTAL CHARITIES</text>
    <rect class="bamboo-art" x="665" y="722" width="20" height="44" opacity="0.85" role="img" aria-label="Small bamboo sprig illustration"/>
    <text class="claim" x="697" y="749">100% natural banboo toothbrush</text>

    <!-- Front panel product title -->
    <text class="product-title" x="554" y="682">BAMBOO TOOTHBRUSH</text>
    <rect class="bamboo-art" x="832" y="632" width="72" height="82" opacity="0.9" role="img" aria-label="Bamboo stalks and leaves illustration"/>
    <circle class="pack-badge" cx="826" cy="697" r="11" stroke="var(--paper)" stroke-width="1.5"/>
    <text class="pack-num" x="826" y="697" text-anchor="middle">4</text>
    <text class="pack-word" x="826" y="704" text-anchor="middle">pack</text>

    <!-- Back panel product title -->
    <text class="product-title" x="554" y="824">BAMBOO TOOTHBRUSH</text>
    <rect class="bamboo-art" x="832" y="774" width="72" height="82" opacity="0.9" role="img" aria-label="Bamboo stalks and leaves illustration"/>
    <circle class="pack-badge" cx="828" cy="838" r="11" stroke="var(--paper)" stroke-width="1.5"/>
    <text class="pack-num" x="828" y="838" text-anchor="middle">4</text>
    <text class="pack-word" x="828" y="845" text-anchor="middle">pack</text>
  </g>
</svg>
</body>
</html>
```